Brochure required for large legal practice

We require a brochure, poster and PowerPoint to be designed to promote our new Employee Benefits Program to our employees. The brochure needs to be modern, clean and corporate. Our target market is solicitors, legal support staff and administration staff based across multiple sites in Queensland, Australia. Logos and brochure/poster content have been attached as well as a detailed brief.

Please note that several photos of our employees have now been uploaded and can be used in this material only.                             

Legal

```html
<!DOCTYPE html>
<html lang="en">
<head>
<meta charset="utf-8">
<title>Brennan Group – Employee Benefits Program Brochure</title>
<link rel="stylesheet" href="https://fonts.googleapis.com/css2?family=Lato:wght@300;400;700&display=swap">
<style>
  :root {
    --stage: #ececec;
    --ink: #3a3a3a;
    --muted: #8a8a8a;
    --black: #1c1c1c;
    --paper: #f6f6f6;
    --paper-edge: #dcdcdc;
    --health: #7aa72a;
    --financial: #ee8a1c;
    --social: #1f63a6;
    --reward: #c8202b;
    --photo-warm: #b9a89a;
    --photo-cool: #9aa6b2;
  }
  * { box-sizing: border-box; margin: 0; padding: 0; }
  html, body { width: 1065px; height: 1200px; overflow: hidden; }
  body { background: var(--stage); font-family: "Lato", sans-serif; color: var(--ink); position: relative; }

  .page { position: absolute; width: 250px; height: 354px; overflow: hidden;
    background: linear-gradient(110deg, #e9e9e9 0%, var(--paper) 45%, #ffffff 100%); }
  .sheet { position: absolute; box-shadow: 0 6px 18px rgba(0,0,0,.18); }
  .spread { width: 500px; height: 354px; }
  .spread .page:first-child { left: 0; background: linear-gradient(90deg, #ffffff 0%, var(--paper) 70%, #dedede 100%); }
  .spread .page:last-child { left: 250px; background: linear-gradient(90deg, #d8d8d8 0%, var(--paper) 12%, #ffffff 100%); }
  .footer-band { position: absolute; left: 0; right: 0; bottom: 0; height: 20px;
    background: linear-gradient(180deg, #4a4a4a, #262626); }
  .footer-band .email { position: absolute; right: 12px; top: 7px; font-size: 5px; color: #9a9a9a; }
  .footer-band .email.left { left: 12px; right: auto; }

  .brand { position: absolute; display: flex; align-items: center; gap: 4px;
    font-size: 7px; font-weight: 700; letter-spacing: .5px; color: var(--muted); text-transform: uppercase; }
  .brand i { width: 7px; height: 7px; background: currentColor; display: block; }
  .brand.light { color: #ffffff; }

  .photo { position: absolute; display: block; }
  .heading { position: absolute; font-weight: 400; text-transform: uppercase; line-height: 1.05; }
  .heading.health { color: var(--health); }
  .heading.financial { color: var(--financial); }
  .heading.social { color: var(--social); }
  .heading.reward { color: var(--reward); }
  .copy { position: absolute; font-size: 5px; line-height: 1.55; color: #7b7b7b; }
  .copy .lead { display: block; font-weight: 700; color: #3d3d3d; margin-bottom: 4px; font-size: 5.3px; }
  .copy p { margin-bottom: 4px; }
  .hl-health { color: var(--health); font-weight: 700; }
  .hl-financial { color: var(--financial); font-weight: 700; }
  .hl-reward { color: var(--reward); font-weight: 700; }

  .ticks { position: absolute; list-style: none; font-size: 5px; line-height: 1.5; color: #7b7b7b; }
  .ticks li { display: flex; gap: 4px; align-items: flex-start; margin-bottom: 5px; }
  .ticks svg { flex: none; width: 7px; height: 7px; margin-top: 1px; }

  /* cover */
  .cover .dark { position: absolute; left: 0; top: 0; width: 250px; height: 218px; background: var(--black); }
  .cover .title { position: absolute; right: 14px; top: 18px; text-align: right; color: #f2f2f2;
    font-weight: 300; font-size: 13px; line-height: 1.3; text-transform: uppercase; }

  /* intro page */
  .intro-title { position: absolute; left: 14px; top: 232px; font-size: 17px; font-weight: 400; line-height: 1.1; color: #2c2c2c; text-transform: uppercase; }
  .intro-rule { position: absolute; left: 14px; right: 30px; top: 276px; height: 1px; background: #bdbdbd; }
  .pillars { position: absolute; left: 14px; top: 282px; font-size: 5px; text-transform: uppercase; white-space: nowrap; }
  .pillars span { margin-right: 3px; }
  .pillars .sep { color: #9a9a9a; }
  .intro-note { position: absolute; left: 14px; top: 300px; font-size: 5px; color: #8a8a8a; }

  .overview-title { position: absolute; left: 24px; top: 62px; font-size: 14px; color: #2c2c2c; text-transform: uppercase; }
  .overview-rule { position: absolute; left: 24px; width: 150px; top: 82px; height: 1px; background: #bdbdbd; }

  /* back cover */
  .back .dark { position: absolute; left: 0; top: 0; width: 250px; height: 300px; background: linear-gradient(160deg, #3a3a3a, var(--black) 60%); }
  .back .contact { position: absolute; left: 0; right: 0; top: 228px; text-align: center; color: #d8d8d8; font-size: 5px; line-height: 1.7; }
  .back .contact .mark { width: 9px; height: 9px; background: #d8d8d8; margin: 0 auto 4px; }
  .back .contact .label { font-weight: 700; letter-spacing: .8px; font-size: 5.5px; }
  .back .contact hr { border: 0; height: 1px; background: #6a6a6a; width: 90px; margin: 3px auto 4px; }

  .globes { position: absolute; list-style: none; font-size: 5px; line-height: 1.45; color: var(--reward); }
  .globes li { display: flex; gap: 4px; margin-bottom: 6px; align-items: flex-start; }
  .globes b { flex: none; width: 7px; height: 7px; border-radius: 50%; background: radial-gradient(circle at 35% 35%, #9fd0f2, #2a78c2); margin-top: 1px; }
</style>
</head>
<body>

<!-- Front cover -->
<section class="sheet page cover" style="left:12px; top:226px;">
  <div class="dark"></div>
  <h1 class="title">Employee Benefits<br>Program</h1>
  <div class="brand light" style="right:16px; top:196px;"><i></i>Brennan Group</div>
  <div class="photo" role="img" aria-label="Four staff members in business attire standing together in an office"
       style="left:0; top:218px; width:250px; height:136px; background:linear-gradient(180deg,#d9dadb,#a9a7a6);"></div>
</section>

<!-- Intro / program overview spread -->
<section class="sheet spread" style="left:282px; top:226px;">
  <div class="page">
    <h2 class="intro-title">Employee Benefits<br>Program</h2>
    <div class="intro-rule"></div>
    <div class="pillars">
      <span style="color:var(--health)">Health</span><span class="sep">|</span>
      <span style="color:var(--financial)">Financial</span><span class="sep">|</span>
      <span style="color:var(--social)">Social &amp; Community</span><span class="sep">|</span>
      <span style="color:var(--reward)">Reward and Recognition</span>
    </div>
    <p class="intro-note">Delivering you a range of benefits</p>
    <div class="footer-band"></div>
  </div>
  <div class="page">
    <div class="brand" style="left:24px; top:22px;"><i></i>Brennan Group</div>
    <h2 class="overview-title">Program Overview</h2>
    <div class="overview-rule"></div>
    <div class="copy" style="left:24px; top:94px; width:180px;">
      <p>Our new program brings together a range of benefits designed to support you at work and at home. Read on to see what is on offer.</p>
      <p>Every employee across our Queensland offices can take part, from day one of employment.</p>
      <p>Speak with your office manager or contact the program team to learn how to enrol.</p>
    </div>
    <div class="footer-band"><span class="email">c.whitfield@brennanlegal.com.au</span></div>
  </div>
</section>

<!-- Back cover -->
<section class="sheet page back" style="left:802px; top:226px;">
  <div class="dark"></div>
  <div class="contact">
    <div class="mark"></div>
    <div class="label">CONTACT</div>
    <hr>
    <div>Brennan Group Employee Benefits Program</div>
    <div>Clara Whitfield</div>
    <div>c.whitfield@brennanlegal.com.au</div>
  </div>
  <div class="brand" style="left:16px; top:322px; color:#555;"><i></i>Brennan Group</div>
</section>

<!-- Health / Financial spread -->
<section class="sheet spread" style="left:22px; top:620px;">
  <div class="page">
    <div class="brand" style="left:14px; top:16px;"><i></i>Brennan Group</div>
    <div class="photo" role="img" aria-label="Red apple" style="left:132px; top:16px; width:50px; height:54px; border-radius:50%; background:radial-gradient(circle at 35% 35%,#e85a5a,#a3141a 70%);"></div>
    <h2 class="heading health" style="left:14px; top:80px; font-size:16px;">Health</h2>
    <div class="copy" style="left:14px; top:102px; width:104px;">
      <span class="lead">Looking after your health and wellbeing, at work and beyond.</span>
      <p>Access flu vaccinations, health checks and <span class="hl-health">discounted gym memberships</span> across all sites.</p>
      <p>Confidential support is available to you and your family at any time.</p>
    </div>
    <div class="photo" role="img" aria-label="Father carrying a child outdoors" style="left:124px; top:104px; width:52px; height:56px; background:linear-gradient(160deg,#a8b98e,#7c6a5a);"></div>
    <div class="photo" role="img" aria-label="Running shoes and measuring tape" style="left:180px; top:104px; width:54px; height:40px; background:linear-gradient(160deg,#e4e4e4,#9a9a8a);"></div>
    <div class="photo" role="img" aria-label="Handshake" style="left:180px; top:148px; width:54px; height:30px; background:linear-gradient(160deg,#c9ccd6,#a58d7c);"></div>
    <div class="photo" role="img" aria-label="Two colleagues smiling at a desk" style="left:14px; top:214px; width:104px; height:92px; background:linear-gradient(160deg,#d8d4cf,#5a4f4a);"></div>
    <div class="copy" style="left:126px; top:200px; width:108px;">
      <span class="lead">Support when you need it most.</span>
      <p>Our assistance program offers <span class="hl-health">free counselling</span> sessions each year.</p>
    </div>
    <div class="footer-band"><span class="email left">c.whitfield@brennanlegal.com.au</span></div>
  </div>
  <div class="page">
    <div class="brand" style="left:20px; top:18px;"><i></i>Brennan Group</div>
    <h2 class="heading financial" style="right:18px; top:18px; font-size:14px;">Financial</h2>
    <div class="copy" style="left:130px; top:40px; width:104px;">
      <span class="lead">Helping you plan and grow your financial future.</span>
      <p>Salary packaging, super advice and banking offers are available to all staff.</p>
      <p><span class="hl-financial">Ask us about</span> novated leasing.</p>
    </div>
    <div style="position:absolute; left:20px; top:64px; font-size:5.5px; font-weight:700; color:#3d3d3d; text-transform:uppercase;">Featured Highlight</div>
    <ul class="ticks" style="left:20px; top:78px; width:96px;">
      <li><svg viewBox="0 0 10 10"><path d="M1 5.5l3 3 5-7" fill="none" stroke="#7aa72a" stroke-width="2"/></svg>Free financial planning session</li>
      <li><svg viewBox="0 0 10 10"><path d="M1 5.5l3 3 5-7" fill="none" stroke="#7aa72a" stroke-width="2"/></svg>Salary packaging options</li>
      <li><svg viewBox="0 0 10 10"><path d="M1 5.5l3 3 5-7" fill="none" stroke="#7aa72a" stroke-width="2"/></svg>Discounted home loans</li>
      <li><svg viewBox="0 0 10 10"><path d="M1 5.5l3 3 5-7" fill="none" stroke="#7aa72a" stroke-width="2"/></svg>Income protection cover</li>
    </ul>
    <div class="photo" role="img" aria-label="Smiling staff member in glasses" style="left:136px; top:200px; width:98px; height:74px; background:linear-gradient(160deg,#d3d6d8,#8a7b6e);"></div>
    <div class="footer-band"></div>
  </div>
</section>

<!-- Social & Community / Reward and Recognition spread -->
<section class="sheet spread" style="left:542px; top:620px;">
  <div class="page">
    <div class="brand" style="left:14px; top:18px;"><i></i>Brennan Group</div>
    <div class="photo" role="img" aria-label="Group of staff standing together" style="left:120px; top:14px; width:114px; height:66px; background:linear-gradient(180deg,#f2f2f2,#8f8478);"></div>
    <h2 class="heading social" style="left:14px; top:86px; font-size:13px;">Social &amp;<br>Community</h2>
    <div class="copy" style="left:14px; top:122px; width:104px;">
      <span class="lead">Building connections across our teams and our community.</span>
      <p>Join staff clubs, social events and charity days held through the year.</p>
    </div>
    <ul class="ticks" style="left:14px; top:166px; width:104px;">
      <li><svg viewBox="0 0 10 10"><path d="M1 5.5l3 3 5-7" fill="none" stroke="#7aa72a" stroke-width="2"/></svg>Annual volunteering leave</li>
      <li><svg viewBox="0 0 10 10"><path d="M1 5.5l3 3 5-7" fill="none" stroke="#7aa72a" stroke-width="2"/></svg>Sports and social club</li>
      <li><svg viewBox="0 0 10 10"><path d="M1 5.5l3 3 5-7" fill="none" stroke="#7aa72a" stroke-width="2"/></svg>Workplace giving program</li>
    </ul>
    <div class="copy" style="left:128px; top:122px; width:106px;">
      <span class="lead">Giving back together.</span>
      <p>We partner with <span class="hl-health">local charities</span> in every region we work in.</p>
      <p>Ask your office about events near you.</p>
    </div>
    <div class="photo" role="img" aria-label="Two colleagues standing by the waterfront" style="left:14px; top:234px; width:220px; height:84px; background:linear-gradient(180deg,#c8d2da 0%,#9aa6ae 55%,#6f6a4e 100%);"></div>
    <div class="footer-band"><span class="email left">c.whitfield@brennanlegal.com.au</span></div>
  </div>
  <div class="page">
    <div class="brand" style="left:16px; top:18px;"><i></i>Brennan Group</div>
    <h2 class="heading reward" style="right:18px; top:14px; font-size:13px; text-align:right;">Reward and<br>Recognition</h2>
    <div class="photo" role="img" aria-label="Two staff members receiving an award in front of a company sign" style="left:16px; top:48px; width:90px; height:112px; background:linear-gradient(160deg,#2a6fb0,#1b3c66 55%,#6b6b6b);"></div>
    <div class="copy" style="left:114px; top:50px; width:120px;">
      <span class="lead">Celebrating great work and long service.</span>
      <p>Colleagues can nominate one another for awards each quarter.</p>
      <p><span class="hl-reward">Service milestones</span> are marked with gifts and leave.</p>
    </div>
    <div class="photo" role="img" aria-label="Gold trophy and award ribbon" style="left:54px; top:196px; width:48px; height:58px; background:linear-gradient(180deg,#e7c45a,#9a7420);"></div>
    <ul class="globes" style="left:136px; top:186px; width:100px;">
      <li><b></b>Quarterly peer awards</li>
      <li><b></b>Service milestone gifts</li>
      <li><b></b>Annual excellence awards</li>
      <li><b></b>Extra leave days</li>
    </ul>
    <div class="footer-band"></div>
  </div>
</section>

</body>
</html>
```